WP website design (N Kentucky)

We need a wordpress design that will incorporate a professional color scheme with company logo in a clean layout. The design needs to consider that this will be developed on a responsive theme. Colors are undetermined - can use a dark red - logo is black so creative use of colors will be important. Client wants a 'modern' look.
Updates

Project Deadline Extended
Reason: Client wants a few more designs

Industry/Entity Type

It Company

Font styles to use
Serif
Sans Serif

Requirements
Must have
• Must Have:
- Navigation: 1) Home 2) Auctions 3) Auction Marketing 4) Buying at Auction 5) About Us 6) Contact Us

Site will have a slideshow element and the following widgets: 1) Featured Auctions 2) Testimonials blog widget 3) 'Auction Alerts' email sign up 4) Fz Chirpa Zelnix+ icons. Colors can be the meadowline7 gold/black from http://www.brambleridgehouses.example/

In the footer, there will be smaller company logo, the affiliations logo, and contact info below:
Copperfield Gavel Sales, LLC / Wes Pellham
email: wespell@mailbox.example; wes.pellham@ml7.example
phone: (859) 555-0147 mobile phone: (859)555-0182
Domain: http://www.copperfieldgavelsales.example/
Nice to have
• - - Site will have drop-down menus - please indicate the styling, for instance the dropdown menus 1) Upcoming Auctions 2) Past Auctions under the 'Auctions' link

```html
<!DOCTYPE html>
<html lang="en">
<head>
<meta charset="utf-8">
<title>Copperfield Gavel Sales</title>
<link rel="stylesheet" href="https://fonts.googleapis.com/css2?family=Roboto:wght@400;500;700&family=Lobster&display=swap">
<style>
:root{
  --red:#e8354f;
  --red-dark:#c92a42;
  --ink:#111;
  --black:#000;
  --white:#fff;
  --grey:#e4e4e4;
  --text:#333;
  --muted:#777;
}
*{box-sizing:border-box;margin:0;padding:0}
html,body{width:930px;height:1200px;overflow:hidden;background:var(--white)}
body{font-family:'Roboto',sans-serif;color:var(--text)}
.page{position:relative;width:930px;height:1200px;overflow:hidden}
.abs{position:absolute}
.city-photo{left:0;top:0;width:930px;height:528px;background:linear-gradient(180deg,#d8d6d8 0%,#bfbac0 14%,#6e6e78 30%,#3c4150 55%,#2a2d36 80%,#30323a 100%)}
.top-line{left:0;top:0;width:930px;height:3px;background:var(--red)}
.logo{left:134px;top:20px;display:flex;align-items:center;gap:8px}
.logo-dot{width:26px;height:26px;border-radius:50%;background:var(--ink)}
.logo-name{font-size:13px;font-weight:700;color:var(--ink);line-height:1.2;width:120px}
.phone{left:518px;top:32px;font-size:14px;color:#333;display:flex;align-items:center;gap:6px}
.search{left:636px;top:26px;width:161px;height:28px;display:flex}
.search-field{flex:1;background:var(--white);border:1px solid #ddd;font-size:10px;color:#555;padding:8px 9px}
.search-btn{width:27px;background:var(--red);display:flex;align-items:center;justify-content:center}
.nav{left:134px;top:73px;height:44px;display:flex}
.nav-item{height:44px;display:flex;align-items:center;justify-content:center;background:var(--red);color:var(--white);font-size:12px;border-right:1px solid var(--red-dark)}
.nav-item.active{background:#2b2b2b}
.dropdown{left:215px;top:118px;width:91px;background:var(--red);box-shadow:0 2px 4px rgba(0,0,0,.4)}
.dropdown div{font-size:8px;color:var(--white);text-align:center;padding:6px 0}
.dropdown div+div{border-top:1px solid var(--red-dark)}
.hero-title{left:0;width:930px;top:242px;text-align:center;font-family:'Lobster',cursive;font-size:30px;color:var(--white)}
.hero-sub{left:0;width:930px;top:297px;text-align:center;font-size:18px;color:var(--white)}
.filter-bar{left:0;top:434px;width:930px;height:94px;background:rgba(40,40,44,.55)}
.filter-label{top:456px;font-size:8.5px;color:var(--white)}
.select{top:476px;height:27px;background:var(--white);display:flex}
.select span{flex:1;font-size:8px;color:#666;padding:9px 8px}
.select i{width:27px;background:var(--red);display:flex;align-items:center;justify-content:center}
.filter-btn{left:733px;top:477px;width:63px;height:24px;background:#1a1a1a;color:var(--white);font-size:10px;display:flex;align-items:center;justify-content:center}
.featured{left:0;top:528px;width:930px;height:286px;background:var(--black)}
.section-title{font-size:14px;color:var(--white)}
.card-photo{top:584px;width:203px;height:126px;border:3px solid var(--white)}
.card-info{top:724px;width:188px;font-size:10px;color:var(--white);line-height:17px}
.card-price{position:absolute;right:0;top:0;color:var(--red)}
.card-zoom{position:absolute;right:0;top:26px;width:30px;height:30px;border-radius:50%;background:var(--white);display:flex;align-items:center;justify-content:center}
.alerts-title,.testi-title{font-size:12px;color:#222}
.alerts-box{left:138px;top:864px;width:228px;height:128px;background:var(--red);border:3px solid var(--white);box-shadow:0 0 3px rgba(0,0,0,.4)}
.field{left:162px;width:186px;height:32px;background:var(--white);font-size:10px;color:#555;padding:10px 11px}
.signup{left:212px;top:954px;width:91px;height:26px;background:#1d1d1d;border-radius:5px;color:var(--white);font-size:10px;display:flex;align-items:center;justify-content:center}
.testi-box{left:378px;top:865px;width:417px;height:128px;background:#efefef;border:2px solid var(--white);box-shadow:0 0 3px rgba(0,0,0,.35)}
.testi-photo{left:380px;top:867px;width:170px;height:124px;background:linear-gradient(160deg,#8aa86a,#5c7a44 55%,#6d6a5c)}
.quote{left:567px;top:884px;width:215px;font-size:7.5px;line-height:16px;color:#666}
.share{top:962px;display:flex;align-items:center;gap:3px;font-size:7px;color:#444}
.share b{font-weight:500;background:var(--white);border:1px solid #ccc;border-radius:2px;padding:2px 4px}
.share span{background:var(--white);border:1px solid #ccc;padding:2px 4px}
.footer{left:0;top:1012px;width:930px;height:106px;background:var(--grey)}
.foot-head{top:1026px;font-size:11px;color:var(--red)}
.foot-text{left:321px;top:1048px;font-size:11px;line-height:15.5px;color:#222}
.badge{top:1053px;height:33px;background:#222}
.bottom{left:0;top:1118px;width:930px;height:82px;background:var(--black)}
.copyright{left:136px;top:1154px;font-size:11px;color:#ccc}
.social{top:1144px;width:29px;height:29px;border-radius:50%;border:2px solid #ddd;color:var(--white);font-size:8px;font-weight:700;display:flex;align-items:center;justify-content:center}
</style>
</head>
<body>
<div class="page">
  <div class="abs city-photo" role="img" aria-label="Evening city skyline with high-rise towers under a pale sky"></div>
  <div class="abs top-line"></div>

  <div class="abs logo"><span class="logo-dot"></span><span class="logo-name">Copperfield Gavel Sales</span></div>
  <div class="abs phone">
    <svg width="15" height="15" viewBox="0 0 16 16"><circle cx="8" cy="8" r="7" fill="none" stroke="#e8354f" stroke-width="1.4"/><path d="M5.3 4.5l1.4 1.6-.8 1c.6 1.2 1.5 2.1 2.7 2.7l1-.8 1.6 1.4-.9 1.2C7.6 11.2 4.8 8.4 4.1 5.4z" fill="#e8354f"/></svg>
    (859)555-0182
  </div>
  <div class="abs search">
    <div class="search-field">Search..</div>
    <div class="search-btn"><svg width="13" height="13" viewBox="0 0 14 14"><circle cx="5.5" cy="5.5" r="4" fill="none" stroke="#fff" stroke-width="1.6"/><path d="M8.5 8.5l4 4" stroke="#fff" stroke-width="2"/></svg></div>
  </div>

  <nav class="abs nav">
    <div class="nav-item active" style="width:81px">Home</div>
    <div class="nav-item" style="width:91px">Auctions</div>
    <div class="nav-item" style="width:147px">Auction Marketing</div>
    <div class="nav-item" style="width:143px">Buying at Auction</div>
    <div class="nav-item" style="width:96px">About Us</div>
    <div class="nav-item" style="width:105px;border-right:0">Contact Us</div>
  </nav>
  <div class="abs dropdown"><div>Upcoming Auctions</div><div>Past Auctions</div></div>

  <svg class="abs" style="left:54px;top:257px" width="31" height="31" viewBox="0 0 31 31"><circle cx="15.5" cy="15.5" r="14" fill="none" stroke="#fff" stroke-width="2.2"/><path d="M18 9.5l-6 6 6 6" fill="none" stroke="#fff" stroke-width="2.4"/></svg>
  <svg class="abs" style="left:844px;top:257px" width="31" height="31" viewBox="0 0 31 31"><circle cx="15.5" cy="15.5" r="14" fill="none" stroke="#fff" stroke-width="2.2"/><path d="M13 9.5l6 6-6 6" fill="none" stroke="#fff" stroke-width="2.4"/></svg>
  <div class="abs hero-title">Lorem Ipsum is simply dummy text of the printing</div>
  <div class="abs hero-sub">Lorem Ipsum is simply dummy text of the printing</div>

  <div class="abs filter-bar"></div>
  <div class="abs filter-label" style="left:133px">PROPERTY TYPE</div>
  <div class="abs filter-label" style="left:330px">LOCATION</div>
  <div class="abs filter-label" style="left:527px">PRICE</div>
  <div class="abs select" style="left:133px;width:184px"><span>All Types</span><i><svg width="9" height="6"><path d="M0 0h9L4.5 6z" fill="#fff"/></svg></i></div>
  <div class="abs select" style="left:330px;width:184px"><span>All Locations</span><i><svg width="9" height="6"><path d="M0 0h9L4.5 6z" fill="#fff"/></svg></i></div>
  <div class="abs select" style="left:527px;width:183px"><span>All Prices</span><i><svg width="9" height="6"><path d="M0 0h9L4.5 6z" fill="#fff"/></svg></i></div>
  <div class="abs filter-btn">SEARCH</div>

  <section class="abs featured"></section>
  <div class="abs section-title" style="left:134px;top:552px">FEATURED AUCTIONS</div>
  <svg class="abs" style="left:762px;top:551px" width="36" height="16" viewBox="0 0 36 16"><circle cx="8" cy="8" r="7" fill="none" stroke="#fff" stroke-width="1.4"/><path d="M9.5 5l-3 3 3 3" fill="none" stroke="#fff" stroke-width="1.5"/><circle cx="27" cy="8" r="7" fill="none" stroke="#fff" stroke-width="1.4"/><path d="M25.5 5l3 3-3 3" fill="none" stroke="#fff" stroke-width="1.5"/></svg>

  <div class="abs card-photo" style="left:135px;background:linear-gradient(180deg,#8fb4d8 0%,#b9cbd8 35%,#6b6a66 60%,#4b4c4a 100%)" role="img" aria-label="Two-storey grey suburban house with a driveway"></div>
  <div class="abs card-photo" style="left:362px;background:linear-gradient(180deg,#9cb8d4 0%,#8c8f88 40%,#6e5f50 75%,#4e4a44 100%)" role="img" aria-label="Cutaway view of a house showing its interior rooms"></div>
  <div class="abs card-photo" style="left:591px;background:linear-gradient(180deg,#1c3f8c 0%,#3b5aa0 30%,#c9b98a 55%,#3f7a2e 80%,#2d5fb0 100%)" role="img" aria-label="Luxury villa lit at dusk with a pool and lawn"></div>

  <div class="abs card-info" style="left:134px">2644 RIDGECREST LN<br>COVINGTON, KY<br>3 BR, 2 BA, SQFT<span class="card-price">$325 K</span><span class="card-zoom"><svg width="17" height="17" viewBox="0 0 17 17"><circle cx="7" cy="7" r="5" fill="none" stroke="#e8354f" stroke-width="2"/><path d="M10.5 10.5l5 5" stroke="#e8354f" stroke-width="2.6"/></svg></span></div>
  <div class="abs card-info" style="left:362px;width:198px">2644 RIDGECREST LN<br>COVINGTON, KY<br>3 BR, 2 BA, SQFT<span class="card-price">$325 K</span><span class="card-zoom"><svg width="17" height="17" viewBox="0 0 17 17"><circle cx="7" cy="7" r="5" fill="none" stroke="#e8354f" stroke-width="2"/><path d="M10.5 10.5l5 5" stroke="#e8354f" stroke-width="2.6"/></svg></span></div>
  <div class="abs card-info" style="left:593px;width:195px">2644 RIDGECREST LN<br>COVINGTON, KY<br>3 BR, 2 BA, SQFT<span class="card-price">$325 K</span><span class="card-zoom"><svg width="17" height="17" viewBox="0 0 17 17"><circle cx="7" cy="7" r="5" fill="none" stroke="#e8354f" stroke-width="2"/><path d="M10.5 10.5l5 5" stroke="#e8354f" stroke-width="2.6"/></svg></span></div>

  <div class="abs alerts-title" style="left:139px;top:843px">AUCTION ALERTS</div>
  <div class="abs alerts-box"></div>
  <div class="abs field" style="top:878px">NAME</div>
  <div class="abs field" style="top:916px">EMAIL</div>
  <div class="abs signup">SIGN UP</div>

  <div class="abs testi-title" style="left:380px;top:841px">TESTIMONIALS</div>
  <div class="abs testi-box"></div>
  <div class="abs testi-photo" role="img" aria-label="Stone cottage with dormer windows surrounded by flowering shrubs"></div>
  <p class="abs quote">“ Lorem ipsum dolor sit amet, consectetur adipisicing elit, sed do eiusmod tempor incididunt ut labore et dolore magna aliqua. Ut enim ad minim veniam, quis nostrud exercitation ullamco laboris nisi ut aliquip ex ea commodo ”</p>
  <div class="abs share" style="left:567px"><b>Like</b><span>200</span></div>
  <div class="abs share" style="left:637px"><b>Chirp</b><span>200</span></div>
  <div class="abs share" style="left:712px"><b style="color:#e8354f">+1</b><span>200</span></div>

  <footer class="abs footer"></footer>
  <div class="abs logo" style="left:140px;top:1056px"><span class="logo-dot" style="width:22px;height:22px"></span><span class="logo-name" style="font-size:10px;width:95px">Copperfield Gavel Sales</span></div>
  <div class="abs foot-head" style="left:319px">CONTACT</div>
  <p class="abs foot-text">Copperfield Gavel Sales, LLC / Wes Pellham<br>email: wespell@mailbox.example; wes.pellham@ml7.example<br>phone: (859) 555-0147 mobile phone: (859)555-0182</p>
  <div class="abs foot-head" style="left:626px">PARTNER</div>
  <div class="abs badge" style="left:627px;width:28px"></div>
  <div class="abs badge" style="left:668px;width:54px;border-radius:4px"></div>
  <div class="abs badge" style="left:734px;width:60px;border-radius:50%"></div>

  <div class="abs bottom"></div>
  <div class="abs copyright">Copyright © 2014&nbsp; All Rights Reserved</div>
  <div class="abs social" style="left:659px;background:#3b5a9a">Fz</div>
  <div class="abs social" style="left:696px;background:#d6463a">Z+</div>
  <div class="abs social" style="left:732px;background:#2aa3e0">Ch</div>
  <div class="abs social" style="left:769px;background:#f26a1b">RSS</div>
</div>
</body>
</html>
```